FREIGHT FORWARDING FLYER

We need a flyer designed for our company (Brightwater Haulage Global) showing the list of services we offer to hand out to customers. Below is a list of services:<br/><br/>-Ocean/Air Import and Export<br/>-Exhibition Cargo<br/>-Carnet Application<br/>-Project Cargo (OOG/Flatrack/Reefer/DG)<br/>-Customs Clearance<br/>-Door to Door Services<br/>-Cargo Insurance<br/>-Warehousing<br/>-Trucking (LTL/FCL)

Target Market(s)

Customers who have a specific need for freight forwarding, especially customers at exhibitions.

Industry/Entity Type

Freight Forwarding

Colors

Designer to choose colors to be used in the design.

Requirements
Must have
• The services we offer need to pop to the customer and essentially get that interested in the services we offer.

```html
<!DOCTYPE html>
<html lang="en">
<head>
<meta charset="utf-8">
<title>Freight Forwarding Flyer – Brightwater Haulage Global</title>
<link rel="stylesheet" href="https://fonts.googleapis.com/css2?family=Oswald:wght@300;400;500;600&display=swap">
<style>
  :root {
    --stage: #e7e5e2;
    --paper: #f7f6f5;
    --ink-dark: #262932;
    --ink-text: #2b2b2f;
    --accent-red: #e21d25;
    --tile-frame: #ffffff;
  }
  * { box-sizing: border-box; margin: 0; padding: 0; }
  html, body { width: 1200px; height: 800px; overflow: hidden; }
  body {
    background: var(--stage);
    font-family: "Oswald", sans-serif;
    position: relative;
  }
  .flyer {
    position: absolute;
    left: 330px; top: 18px;
    width: 540px; height: 764px;
    background: var(--paper);
    overflow: hidden;
    box-shadow: 0 10px 30px rgba(0,0,0,.18);
  }
  .flyer__backdrop { position: absolute; inset: 0; }
  .flyer__title {
    position: absolute;
    left: 150px; top: 58px;
    font-size: 42px; font-weight: 500;
    letter-spacing: .5px;
    color: #fff;
    text-transform: uppercase;
  }
  .flyer__title .highlight { color: var(--accent-red); }

  .photo-tile {
    position: absolute;
    border: 8px solid var(--tile-frame);
    border-radius: 14px;
    transform: rotate(45deg);
    box-shadow: 0 8px 18px rgba(0,0,0,.3);
    overflow: hidden;
  }
  .photo-tile--ship {
    width: 170px; height: 170px; left: 85px; top: 205px;
    background: linear-gradient(160deg, #7fb0dc 0%, #a9cbe8 40%, #2e6fa8 60%, #1d4d7c 100%);
  }
  .photo-tile--truck {
    width: 130px; height: 130px; left: 305px; top: 185px;
    background: linear-gradient(160deg, #cfe0ee 0%, #9fbcd6 40%, #2a47a3 65%, #5d6b4a 100%);
  }
  .photo-tile--plane {
    width: 160px; height: 160px; left: 330px; top: 320px;
    background: linear-gradient(160deg, #d9574a 0%, #f08a4b 45%, #f6c27a 70%, #b8442f 100%);
  }

  .services {
    position: absolute;
    left: 40px; top: 452px;
    width: 470px; height: 220px;
  }
  .services__heading {
    font-size: 28px; font-weight: 500;
    color: var(--ink-text);
    white-space: nowrap;
  }
  .services__heading .highlight { color: var(--accent-red); }
  .service-list {
    position: absolute;
    list-style: none;
    font-size: 19px; font-weight: 400;
    color: var(--ink-text);
  }
  .service-list li {
    position: relative;
    height: 32px; line-height: 32px;
    padding-left: 22px;
    white-space: nowrap;
  }
  .service-list li::before {
    content: "";
    position: absolute; left: 0; top: 12px;
    width: 9px; height: 9px;
    background: var(--accent-red);
    transform: rotate(20deg);
  }
  .service-list--primary { left: 0; top: 58px; }
  .service-list--secondary { left: 305px; top: 58px; }

  .brand {
    position: absolute;
    left: 40px; bottom: 42px;
    display: flex; align-items: center; gap: 12px;
  }
  .brand__mark {
    width: 22px; height: 22px;
    background: var(--accent-red);
  }
  .brand__name {
    font-size: 26px; font-weight: 500;
    color: var(--ink-text);
    text-transform: uppercase;
    letter-spacing: .5px;
  }
</style>
</head>
<body>
  <article class="flyer">
    <svg class="flyer__backdrop" width="540" height="764" viewBox="0 0 540 764" aria-hidden="true">
      <polygon class="header-band" points="0,0 540,0 540,300 0,430" fill="#262932"/>
      <polyline class="chevron chevron--top" points="30,10 80,55 130,10" fill="none" stroke="#fff" stroke-width="16"/>
      <polyline class="chevron chevron--right" points="440,120 478,160 520,118" fill="none" stroke="#fff" stroke-width="14"/>
      <rect class="accent-square" x="275" y="150" width="18" height="18" fill="#e21d25" transform="rotate(30 284 159)"/>
      <rect class="accent-square" x="22" y="330" width="14" height="14" fill="#e21d25" transform="rotate(30 29 337)"/>
      <rect class="accent-square" x="440" y="195" width="16" height="16" fill="#e21d25" transform="rotate(30 448 203)"/>
      <rect class="accent-outline" x="470" y="255" width="34" height="34" fill="none" stroke="#e21d25" stroke-width="6" transform="rotate(30 487 272)"/>
    </svg>

    <h1 class="flyer__title">Freight <span class="highlight">Forwarding</span></h1>

    <div class="photo-tile photo-tile--ship" role="img" aria-label="Container ship loaded with cargo at sea under a blue sky"></div>
    <div class="photo-tile photo-tile--truck" role="img" aria-label="Blue semi truck on the road"></div>
    <div class="photo-tile photo-tile--plane" role="img" aria-label="Cargo airplane taking off against an orange sunset sky"></div>

    <section class="services">
      <h2 class="services__heading">Below Is A <span class="highlight">List Of Services</span></h2>
      <ul class="service-list service-list--primary">
        <li>Exhibition Cargo</li>
        <li>Carnet Application</li>
        <li>Customs Clearance</li>
        <li>Ocean/Air Import &amp; Export</li>
        <li>Project Cargo (OOG/Flatrack/Reefer/DG)</li>
      </ul>
      <ul class="service-list service-list--secondary">
        <li>Door to Door Services</li>
        <li>Cargo Insurance</li>
        <li>Warehousing</li>
        <li>Trucking (LTL/FCL)</li>
      </ul>
    </section>

    <footer class="brand">
      <span class="brand__mark"></span>
      <span class="brand__name">Brightwater Haulage Global</span>
    </footer>
  </article>
</body>
</html>
```